RW Frameworks Inc Business cards

We need business cards using our existing logo but slightly modified. Right now the logo says RW Framework Masonry. We want to keep the RW part of the design, but replace the Framework Masonry portion with "FRAMEWORKS". Please see the attached file.
Ideally this would be a blank template so we can add Different Names, titles, and phone numbers later.
On the one side we want only the logo and on the other side the detail. I'm attaching an example for you to see.
Please reach out with any other questions. Our address and other details will be given out once we find a design we like.

Target Market(s)

Construction Industry

```html
<!DOCTYPE html>
<html lang="en">
<head>
<meta charset="UTF-8">
<title>RW Frameworks Inc — Business Cards</title>
<link href="https://fonts.googleapis.com/css2?family=Barlow+Condensed:wght@600&family=Montserrat:wght@300;400&display=swap" rel="stylesheet">
<style>
  :root {
    --backdrop: #c9cccf;
    --brand-blue: #1562b9;
    --brand-navy: #0c2d79;
    --brand-grey: #646567;
    --paper: #f1f1f1;
    --title-grey: #a9b3c4;
  }
  * { margin: 0; padding: 0; box-sizing: border-box; }
  html, body {
    width: 1023px;
    height: 1200px;
    overflow: hidden;
    background: var(--backdrop);
  }
  .canvas {
    position: relative;
    width: 1023px;
    height: 1200px;
  }
  .card {
    position: absolute;
    left: 158px;
    width: 707px;
    height: 404px;
    overflow: hidden;
  }
  .card--front { top: 123px; background: var(--brand-blue); }
  .card--back  { top: 610px; background: var(--paper); }

  .front-panel {
    position: absolute;
    inset: 0;
    width: 707px;
    height: 404px;
  }

  .wordmark {
    position: absolute;
    font-family: "Barlow Condensed", sans-serif;
    font-weight: 600;
    line-height: 1;
    white-space: nowrap;
  }
  .wordmark__initials { display: block; }
  .wordmark__name { display: block; }

  .card--front .wordmark {
    right: 40px;
    top: 160px;
    color: var(--paper);
    text-align: right;
  }
  .card--front .wordmark__initials { font-size: 178px; letter-spacing: 10px; margin-right: -10px; }
  .card--front .wordmark__name { font-size: 60px; letter-spacing: 8.6px; margin-right: -8.6px; margin-top: -10px; }

  .card--back .wordmark {
    left: 230px;
    top: 36px;
    width: 247px;
    color: var(--brand-blue);
    text-align: center;
  }
  .card--back .wordmark__initials { font-size: 132px; letter-spacing: 8px; margin-right: -8px; }
  .card--back .wordmark__name { font-size: 45px; letter-spacing: 6.3px; margin-right: -6.3px; margin-top: -8px; }

  .name-band {
    position: absolute;
    left: 0;
    top: 217px;
    width: 100%;
    height: 64px;
    background: var(--brand-blue);
    padding-left: 36px;
    display: flex;
    align-items: center;
    gap: 8px;
  }
  .person-name {
    font-family: "Barlow Condensed", sans-serif;
    font-weight: 600;
    font-size: 44px;
    color: var(--paper);
    letter-spacing: 0.3px;
    line-height: 1;
    padding-top: 6px;
  }
  .person-title {
    font-family: "Montserrat", sans-serif;
    font-weight: 300;
    font-size: 22px;
    color: var(--title-grey);
    padding-top: 14px;
  }

  .contact-band {
    position: absolute;
    left: 0;
    top: 281px;
    width: 100%;
    height: 123px;
    background: var(--brand-navy);
    font-family: "Montserrat", sans-serif;
    font-weight: 300;
    font-size: 20px;
    color: var(--paper);
    line-height: 28px;
  }
  .contact-list {
    position: absolute;
    left: 36px;
    top: 16px;
    list-style: none;
  }
  .contact-address {
    position: absolute;
    left: 428px;
    top: 49px;
    font-style: normal;
    line-height: 27px;
  }
</style>
</head>
<body>
<main class="canvas">

  <section class="card card--front" aria-label="Business card front">
    <svg class="front-panel" viewBox="0 0 707 404" aria-hidden="true">
      <polygon points="410,0 707,0 707,404 90,404 90,265" fill="var(--brand-navy)"/>
    </svg>
    <div class="wordmark">
      <span class="wordmark__initials">RW</span>
      <span class="wordmark__name">FRAMEWORKS</span>
    </div>
  </section>

  <section class="card card--back" aria-label="Business card back">
    <div class="wordmark">
      <span class="wordmark__initials">RW</span>
      <span class="wordmark__name">FRAMEWORKS</span>
    </div>

    <div class="name-band">
      <span class="person-name">FIRSTNAME LASTNAME</span>
      <span class="person-title">Title</span>
    </div>

    <div class="contact-band">
      <ul class="contact-list">
        <li>123.456.7890</li>
        <li>info@youremail.com</li>
        <li>yourwebsite.com</li>
      </ul>
      <address class="contact-address">
        123 somewhere,<br>
        City, State 12345
      </address>
    </div>
  </section>

</main>
</body>
</html>
```